RK Brennan & Associates

Create a website encompassing design work already carried out for business card.
Small accounting practice, business accounting and management, superannuation, audit, taxation.

```html
<!DOCTYPE html>
<html lang="en">
<head>
<meta charset="utf-8">
<title>RK Brennan &amp; Associates</title>
<link href="https://fonts.googleapis.com/css2?family=Open+Sans:ital,wght@0,400;0,600;1,400&display=swap" rel="stylesheet">
<style>
:root{
  --ink:#2f2f2f;
  --muted:#666;
  --accent:#5f9fdc;
  --accent-light:#7bb3e8;
  --header:#222222;
  --footer:#2a2a2a;
  --pale:#f5f5f5;
  --white:#ffffff;
  --orange:#e07a2e;
}
*{box-sizing:border-box;margin:0;padding:0}
html,body{width:824px;height:1200px;overflow:hidden}
body{position:relative;font-family:"Open Sans",Arial,sans-serif;color:var(--ink);background:var(--white)}
.abs{position:absolute}

.site-header{left:0;top:0;width:824px;height:92px;background:var(--header)}
.brand{left:140px;top:22px;display:flex;align-items:center;gap:8px;color:var(--white);font-weight:600;font-size:14px;line-height:1}
.brand-mark{width:30px;height:30px;background:var(--accent)}
.brand-tagline{left:89px;top:68px;width:206px;height:14px;background:var(--accent);color:var(--white);font-size:5px;line-height:14px;text-align:center;font-weight:600}
.social-top{top:22px;width:20px;height:20px;border-radius:50%;background:#0d0d0d}
.main-nav{left:0;top:56px;width:824px;height:21px;font-size:9px;color:var(--white)}
.nav-item{position:absolute;top:0;height:21px;line-height:21px}
.nav-item.active{background:var(--accent-light);padding:0 11px}

.hero{left:0;top:92px;width:824px;height:349px;background:linear-gradient(120deg,#6d6f73 0%,#9a9ea4 35%,#c5ccd3 65%,#aab6c1 100%)}
.hero-shade{left:0;top:92px;width:824px;height:349px;background:rgba(20,25,35,.28)}
.hero-title{left:0;top:190px;width:824px;text-align:center;color:var(--white);font-size:30px;font-weight:600;letter-spacing:.5px}
.hero-rule{left:230px;top:236px;width:364px;height:1px;background:rgba(255,255,255,.45)}
.hero-text{left:150px;top:258px;width:524px;text-align:center;color:var(--white);font-size:15px;line-height:25px}
.btn{background:var(--accent-light);color:var(--white);text-align:center}
.hero-btn{left:364px;top:327px;width:96px;height:29px;line-height:29px;font-size:11px}

.services{left:0;top:441px;width:824px;height:264px;background:var(--pale)}
.service{top:497px;width:150px;text-align:center}
.service-icon{width:68px;height:68px;border-radius:50%;background:var(--accent);margin:0 auto;display:flex;align-items:center;justify-content:center}
.service h3{font-weight:400;font-size:16px;margin-top:14px;color:var(--ink)}
.service p{font-size:9px;line-height:15px;color:var(--muted);margin-top:7px}
.service .more{display:inline-block;margin-top:9px;width:44px;height:20px;line-height:20px;font-size:9px;background:var(--accent-light);color:var(--white)}

.welcome-title{left:92px;top:740px;font-size:17px;font-weight:400}
.welcome-text{left:92px;top:778px;width:430px;font-size:9px;line-height:16.5px;color:var(--muted)}
.welcome-btn{left:92px;top:861px;width:79px;height:27px;line-height:27px;font-size:10px}
.team-photo{left:529px;top:755px;width:206px;height:127px;background:linear-gradient(135deg,#e9eef3 0%,#c9d1da 45%,#5b6f86 70%,#d9dee4 100%)}

.testimonials{left:0;top:925px;width:824px;height:221px;background:var(--pale)}
.testimonial-title{left:0;top:949px;width:824px;text-align:center;font-size:17px}
.quote{left:100px;top:987px;width:626px;text-align:center;font-size:8.6px;line-height:19px;color:var(--muted)}
.qmark{font-size:22px;color:#bbb;font-style:italic;font-family:Georgia,serif}
.avatar{left:335px;top:1066px;width:56px;height:56px;border-radius:50%;background:linear-gradient(160deg,#3a2d28 0%,#e6c9b5 55%,#8fb3d9 100%)}
.author{left:404px;top:1076px;font-size:9px;color:var(--orange)}
.author-role{left:404px;top:1092px;font-size:8.5px;font-style:italic;color:var(--muted)}

.site-footer{left:0;top:1146px;width:824px;height:54px;background:var(--footer)}
.copyright{left:91px;top:1168px;font-size:9px;color:#ddd}
.social-foot{top:1164px;width:20px;height:20px;border-radius:50%;border:1.5px solid #cfcfcf}
</style>
</head>
<body>

<header>
  <div class="abs site-header"></div>
  <div class="abs brand"><span class="brand-mark"></span>RK Brennan &amp; Associates</div>
  <div class="abs brand-tagline">Accountant · Business Solutions · Management · Superannuation · Audit</div>
  <span class="abs social-top" style="left:614px"></span>
  <span class="abs social-top" style="left:639px"></span>
  <span class="abs social-top" style="left:664px"></span>
  <span class="abs social-top" style="left:688px"></span>
  <span class="abs social-top" style="left:713px"></span>
  <nav class="abs main-nav">
    <span class="nav-item active" style="left:395px">HOME</span>
    <span class="nav-item" style="left:464px">ABOUT US</span>
    <span class="nav-item" style="left:538px">SERVICES</span>
    <span class="nav-item" style="left:605px">SOLUTIONS</span>
    <span class="nav-item" style="left:683px">CONTACTS</span>
  </nav>
</header>

<section>
  <div class="abs hero" role="img" aria-label="Photo of a calculator, pencil and financial charts"></div>
  <div class="abs hero-shade"></div>
  <h1 class="abs hero-title">RK BRENNAN &amp; ASSOCIATES</h1>
  <div class="abs hero-rule"></div>
  <p class="abs hero-text">We do Small accounting practice, business accounting and management, superannuation, audit, taxation.</p>
  <div class="abs btn hero-btn">Learn More</div>
  <svg class="abs" style="left:63px;top:252px" width="14" height="26"><polyline points="11,2 3,13 11,24" fill="none" stroke="#fff" stroke-width="2.5"/></svg>
  <svg class="abs" style="left:748px;top:252px" width="14" height="26"><polyline points="3,2 11,13 3,24" fill="none" stroke="rgba(255,255,255,.5)" stroke-width="2"/></svg>
</section>

<section>
  <div class="abs services"></div>
  <div class="abs service" style="left:90px">
    <div class="service-icon"><svg width="20" height="24"><rect x="1" y="1" width="18" height="22" fill="none" stroke="#fff" stroke-width="2"/><rect x="4" y="4" width="12" height="4" fill="#fff"/><g fill="#fff"><rect x="4" y="11" width="3" height="3"/><rect x="9" y="11" width="3" height="3"/><rect x="14" y="11" width="2" height="3"/><rect x="4" y="16" width="3" height="3"/><rect x="9" y="16" width="3" height="3"/><rect x="14" y="16" width="2" height="3"/></g></svg></div>
    <h3>Accountant</h3>
    <p>Neque porro quisquam est qui dolorem ipsum dolor.</p>
    <span class="more">More</span>
  </div>
  <div class="abs service" style="left:255px">
    <div class="service-icon"><svg width="30" height="24"><rect x="1" y="5" width="28" height="18" fill="#fff"/><rect x="10" y="1" width="10" height="5" fill="none" stroke="#fff" stroke-width="2"/><polyline points="10,13 14,17 21,10" fill="none" stroke="#5f9fdc" stroke-width="2.5"/></svg></div>
    <h3>Business Solution</h3>
    <p>Neque porro quisquam est qui dolorem ipsum dolor.</p>
    <span class="more">More</span>
  </div>
  <div class="abs service" style="left:420px">
    <div class="service-icon"><svg width="30" height="26"><circle cx="11" cy="7" r="6" fill="#fff"/><circle cx="22" cy="10" r="4.5" fill="#fff"/><path d="M1 26 Q1 14 11 14 Q21 14 21 26Z" fill="#fff"/><path d="M17 26 Q18 17 23 17 Q30 17 30 26Z" fill="#fff"/></svg></div>
    <h3>Management</h3>
    <p>Neque porro quisquam est qui dolorem ipsum dolor.</p>
    <span class="more">More</span>
  </div>
  <div class="abs service" style="left:585px">
    <div class="service-icon"><svg width="30" height="28"><g fill="#fff"><rect x="2" y="18" width="6" height="10"/><rect x="11" y="14" width="6" height="14"/><rect x="20" y="10" width="6" height="18"/></g><polyline points="2,14 10,8 16,11 26,2" fill="none" stroke="#fff" stroke-width="2"/></svg></div>
    <h3>Superannuation</h3>
    <p>Neque porro quisquam est qui dolorem ipsum dolor.</p>
    <span class="more">More</span>
  </div>
  <svg class="abs" style="left:742px;top:563px" width="12" height="22"><polyline points="2,2 10,11 2,20" fill="none" stroke="#c8c8c8" stroke-width="2"/></svg>
</section>

<section>
  <h2 class="abs welcome-title">Welcome to Our Site!</h2>
  <p class="abs welcome-text">Donec nulla libero, bibendum at iaculis id, iaculis vel nunc. Cras elementum risus ac liberol eleifend eges­tas. Proin quis placerat purus. Nunc malesuada tellus at ipsum venenatiquam. Quisque accumsan tellus sit amet nunc porttitor sagittis. Mauris sed lorem volutpattibulum arcu a, pellentesque nulla. Donec suscipit risus neque. Donec nulla libero, bibendum at iaculis id, iaculis vel nunc.</p>
  <div class="abs btn welcome-btn">Learn More</div>
  <div class="abs team-photo" role="img" aria-label="Photo of a smiling business team with a laptop"></div>
</section>

<section>
  <div class="abs testimonials"></div>
  <h2 class="abs testimonial-title" style="font-weight:400">Testimonial</h2>
  <p class="abs quote"><span class="qmark">“</span> Daniel has been an excellent show partner to work with and is always ready to give suggestions and share experiences which helped out greatly in the on stage planning process. He is funny, witty, quick on his feet and great with people. I can't imagine anyone better hosting the Harbour Care Trust Charity Walkathon 2010 other than Daniel. A professional indeed! <span class="qmark">”</span></p>
  <svg class="abs" style="left:293px;top:1084px" width="12" height="20"><polyline points="10,2 3,10 10,18" fill="none" stroke="#999" stroke-width="2"/></svg>
  <div class="abs avatar" role="img" aria-label="Portrait photo of the client"></div>
  <div class="abs author">by Nora Pellington</div>
  <div class="abs author-role">lorem pised tuilhuyqs sit</div>
  <svg class="abs" style="left:529px;top:1084px" width="12" height="20"><polyline points="2,2 9,10 2,18" fill="none" stroke="#ccc" stroke-width="2"/></svg>
</section>

<footer>
  <div class="abs site-footer"></div>
  <div class="abs copyright">Copyright © Yoursite 2014 - All Rights Reserved</div>
  <span class="abs social-foot" style="left:643px"></span>
  <span class="abs social-foot" style="left:666px"></span>
  <span class="abs social-foot" style="left:689px"></span>
  <span class="abs social-foot" style="left:712px"></span>
</footer>

</body>
</html>
```